Copper Lantern Taverna Business Card plus one change to logo design

Hi Marguerite,

OK I am ready to get a business card designed. It should have following on front

Logo
Ilona Brevard-Tesk
Founder

e: ilona@copperlanterntaverna.example
w: www.copperlanterntaverna.example
c: 555-284-7716

On Back:

Copper Lantern Taverna is currently looking for contributors, supporting enterprises, and members-if interested, please get in touch!

I would also like you to change the byline to "for progressive minds with bold ideas"

```html
<!DOCTYPE html>
<html lang="en">
<head>
<meta charset="utf-8">
<title>Copper Lantern Taverna – Business Card</title>
<link rel="stylesheet" href="https://fonts.googleapis.com/css2?family=Open+Sans:ital,wght@0,400;0,600;0,700;1,400&family=Kalam:wght@400&display=swap">
<style>
  :root {
    --bg: #1e1e1e;
    --brand-red: #a82428;
    --ink: #1b1b1b;
    --paper: #ffffff;
    --muted: #3a3a3a;
    --rule-grey: #8a8a8a;
  }
  * { box-sizing: border-box; margin: 0; padding: 0; }
  html, body { width: 1200px; height: 900px; overflow: hidden; background: var(--bg); }
  body { position: relative; font-family: "Open Sans", Arial, sans-serif; }

  .card {
    position: absolute;
    width: 540px;
    height: 309px;
    overflow: hidden;
    box-shadow: 0 14px 30px rgba(0,0,0,.55);
  }

  /* Back of card */
  .card--back { left: 150px; top: 110px; background: var(--brand-red); }
  .back-mark {
    position: absolute; left: 50%; top: 34px; transform: translateX(-50%);
    display: flex; align-items: center; gap: 12px;
    color: var(--paper); font-weight: 700; font-size: 22px; white-space: nowrap;
  }
  .back-mark__square {
    width: 26px; height: 26px; border: 2px solid var(--paper); border-radius: 5px;
  }
  .back-message {
    position: absolute; left: 0; right: 0; top: 178px;
    text-align: center; color: var(--paper);
    font-weight: 700; font-size: 12.5px; line-height: 1.45;
    padding: 0 40px;
  }
  .back-stripes { position: absolute; left: 0; right: 0; bottom: 0; height: 46px; }
  .back-stripes span { position: absolute; left: 0; right: 0; }
  .back-stripes .s-white-1 { top: 0; height: 6px; background: var(--paper); }
  .back-stripes .s-red { top: 6px; height: 4px; background: var(--brand-red); }
  .back-stripes .s-white-2 { top: 10px; height: 3px; background: var(--paper); }
  .back-stripes .s-black { top: 13px; height: 3px; background: var(--ink); }
  .back-stripes .s-white-3 { top: 16px; bottom: 0; background: var(--paper); }

  /* Front of card */
  .card--front { left: 510px; top: 470px; background: var(--paper); }
  .front-stripes { position: absolute; left: 0; top: 0; bottom: 0; width: 34px; }
  .front-stripes span { position: absolute; top: 0; bottom: 0; }
  .front-stripes .f-red-wide { left: 0; width: 18px; background: var(--brand-red); }
  .front-stripes .f-black { left: 22px; width: 3px; background: var(--ink); }
  .front-stripes .f-red-thin { left: 28px; width: 3px; background: var(--brand-red); }

  .brand { position: absolute; left: 70px; top: 40px; }
  .brand__lockup { display: flex; align-items: center; gap: 10px; }
  .brand__square { width: 22px; height: 22px; background: var(--ink); }
  .brand__name { font-weight: 700; font-size: 24px; color: var(--ink); white-space: nowrap; letter-spacing: -.3px; }
  .brand__rule { margin: 6px 0 4px 32px; height: 1px; background: var(--rule-grey); width: 290px; }
  .brand__tagline {
    margin-left: 34px; font-family: "Kalam", "Comic Sans MS", cursive;
    font-size: 13px; color: var(--muted); letter-spacing: .6px; white-space: nowrap;
  }

  .person { position: absolute; left: 92px; top: 222px; }
  .person__name { color: var(--brand-red); font-weight: 700; font-size: 17px; white-space: nowrap; }
  .person__role { color: var(--ink); font-size: 13px; margin-top: 1px; }

  .contact { position: absolute; left: 272px; top: 176px; list-style: none; }
  .contact li { display: flex; align-items: center; gap: 6px; font-size: 11.5px; color: var(--ink); height: 21px; white-space: nowrap; }
  .contact svg { width: 15px; height: 15px; flex: none; }
  .contact strong { font-weight: 700; }
</style>
</head>
<body>

<section class="card card--back" aria-label="Business card, back">
  <div class="back-mark">
    <span class="back-mark__square"></span>
    <span>Copper Lantern Taverna</span>
  </div>
  <p class="back-message">Copper Lantern Taverna is currently looking for contributors,<br>supporting enterprises, and members-if interested, please get in touch!</p>
  <div class="back-stripes">
    <span class="s-white-1"></span><span class="s-red"></span><span class="s-white-2"></span><span class="s-black"></span><span class="s-white-3"></span>
  </div>
</section>

<section class="card card--front" aria-label="Business card, front">
  <div class="front-stripes">
    <span class="f-red-wide"></span><span class="f-black"></span><span class="f-red-thin"></span>
  </div>

  <div class="brand">
    <div class="brand__lockup">
      <span class="brand__square"></span>
      <span class="brand__name">Copper Lantern Taverna</span>
    </div>
    <div class="brand__rule"></div>
    <p class="brand__tagline">for progressive minds with bold ideas</p>
  </div>

  <div class="person">
    <p class="person__name">Ilona Brevard-Tesk</p>
    <p class="person__role">Founder</p>
  </div>

  <ul class="contact">
    <li>
      <svg viewBox="0 0 16 16" aria-hidden="true"><circle cx="8" cy="8" r="7" fill="none" stroke="#a82428" stroke-width="1.6"/><path d="M5.6 4.6c.6 3 2.5 5.2 5.6 6.4l.6-1.4-1.6-.8-.7.8c-1.2-.6-2.1-1.5-2.6-2.7l.8-.7-.8-1.6z" fill="#a82428"/></svg>
      <span>555.284.7716</span>
    </li>
    <li>
      <svg viewBox="0 0 16 16" aria-hidden="true"><circle cx="8" cy="8" r="7" fill="#a82428"/><rect x="4.2" y="5.3" width="7.6" height="5.4" fill="none" stroke="#fff" stroke-width="1"/><path d="M4.2 5.3 8 8.3l3.8-3" fill="none" stroke="#fff" stroke-width="1"/></svg>
      <span>ilona@copperlanterntaverna.example</span>
    </li>
    <li>
      <svg viewBox="0 0 16 16" aria-hidden="true"><circle cx="8" cy="8" r="7" fill="none" stroke="#a82428" stroke-width="1.6"/><circle cx="8" cy="8" r="3.4" fill="none" stroke="#a82428" stroke-width="1"/><path d="M4.6 8h6.8M8 4.6v6.8" stroke="#a82428" stroke-width="1"/></svg>
      <span>www.<strong>copperlanterntaverna</strong>.example</span>
    </li>
  </ul>
</section>

</body>
</html>
```